Plumbing Business Letterhead Design

Need a letterhead designed to use for my invoices and letters. I would like it to incorporate my business logo, which i will upload, and use light blue and grey colours. Or any colours that will work well with my logo (im not very good with art to know) . Also the letterhead needs to include the following:
Address - P.O Box 4826 Kellaby NSW 2631
Email - gareth@rwhitfieldplumbing.example.au
ABN - 41 906 572 338
Licence No. - 582061K
Mobile - 0412076584

Industry/Entity Type

Plumbing

Font styles to use
Sans Serif

Colors

Designer to choose colors to be used in the design.

```html
<!DOCTYPE html>
<html lang="en">
<head>
<meta charset="utf-8">
<title>Gareth Whitfield Plumbing – Letterhead</title>
<link href="https://fonts.googleapis.com/css2?family=Open+Sans:wght@400;600;700&family=Arimo:wght@700&display=swap" rel="stylesheet">
<style>
  :root {
    --backdrop: #e4e5e6;
    --paper: #fafafa;
    --brand-blue: #1fa3de;
    --brand-blue-soft: #8fd0ee;
    --brand-orange: #f18f0f;
    --brand-orange-soft: #f7c27d;
    --ink: #2b2b2b;
    --ink-soft: #3a3a3a;
    --grey-mark: #4a4a4a;
    --sig-tone: #d9d9d9;
  }
  * { box-sizing: border-box; margin: 0; padding: 0; }
  html, body { width: 1200px; height: 945px; overflow: hidden; }
  body {
    background: var(--backdrop);
    font-family: "Open Sans", Arial, sans-serif;
    color: var(--ink);
  }
  .letterhead {
    position: absolute;
    left: 266px; top: 0;
    width: 668px; height: 945px;
    background: var(--paper);
    overflow: hidden;
  }
  .letterhead__header-art {
    position: absolute; left: 0; top: 0;
    width: 668px; height: 64px;
    background: linear-gradient(90deg, var(--brand-blue-soft), var(--brand-blue) 60%, var(--brand-orange-soft));
  }
  .brand {
    position: absolute; left: 44px; top: 112px;
    display: flex; align-items: center; gap: 10px;
  }
  .brand__square {
    width: 44px; height: 44px;
    border: 5px solid var(--grey-mark);
    border-radius: 8px;
  }
  .brand__name {
    font-weight: 700;
    font-size: 20px;
    line-height: 1.05;
    color: var(--grey-mark);
    text-transform: uppercase;
    width: 170px;
  }
  .contact {
    position: absolute; left: 420px; top: 112px;
    font-size: 7.5px; line-height: 1.45;
    color: var(--ink-soft);
    list-style: none;
  }
  .contact__label { color: var(--brand-blue); font-weight: 700; text-transform: uppercase; }
  .letter {
    position: absolute; left: 58px; top: 252px; width: 560px;
  }
  .letter__salutation {
    font-family: "Arimo", Arial, sans-serif;
    font-weight: 700; font-size: 14px; margin-bottom: 12px;
  }
  .letter__para {
    margin-left: 22px;
    font-size: 11.5px; line-height: 1.32;
    color: var(--ink-soft);
    margin-bottom: 14px;
  }
  .signature {
    position: absolute; left: 92px; top: 690px;
    width: 140px; height: 46px;
    background: var(--sig-tone);
    border-radius: 4px;
  }
  .letterhead__footer-rule {
    position: absolute; left: 0; bottom: 0;
    width: 100%; height: 6px;
    background: var(--brand-blue);
  }
</style>
</head>
<body>
  <main class="letterhead">
    <div class="letterhead__header-art" role="img" aria-label="Decorative blue and orange header artwork"></div>

    <div class="brand">
      <span class="brand__square"></span>
      <span class="brand__name">Gareth Whitfield Plumbing</span>
    </div>

    <ul class="contact">
      <li><span class="contact__label">Address</span> - P.O Box 4826 Kellaby NSW 2631</li>
      <li><span class="contact__label">Email</span> - gareth@rwhitfieldplumbing.example.au</li>
      <li><span class="contact__label">ABN No.</span> - 41 906 572 338</li>
      <li><span class="contact__label">Licence No.</span> - 582061K</li>
      <li><span class="contact__label">Mobile</span> - 0412076584</li>
    </ul>

    <section class="letter">
      <p class="letter__salutation">Dear Mr. Delaney,</p>
      <p class="letter__para">Lorem Ipsum is simply dummy text of the printing and typesetting industry. Lorem Ipsum has been the industry's standard dummy text ever since the 1500s, when an unknown printer took a galley of type and scrambled it to make a type specimen book. It has survived not only five centuries, but also the leap into electronic typesetting, remaining essentially unchanged.</p>
      <p class="letter__para">The standard chunk of Lorem Ipsum used since the 1500s is reproduced below for those interested. Sections 1.10.32 and 1.10.33 from "de Finibus Bonorum et Malorum" by Cicero are also reproduced in their exact original form, accompanied by English versions from the 1914 translation by H. Rackham</p>
      <p class="letter__para">Lorem Ipsum is simply dummy text of the printing and typesetting industry. Lorem Ipsum has been the industry's standard dummy text ever since the 1500s, when an unknown printer took a galley of type and scrambled it to make a type specimen book. It has survived not only five centuries, but also the leap into electronic typesetting, remaining essentially unchanged. It was popularised in the</p>
      <p class="letter__para">The standard chunk of Lorem Ipsum used since the 1500s is reproduced below for those interested. Sections 1.10.32 and 1.10.33 from "de Finibus Bonorum et Malorum" by Cicero are also reproduced in their exact original form, accompanied by English versions from the 1914 translation by H. Rackham</p>
      <p class="letter__para">The standard chunk of Lorem Ipsum used since the 1500s is reproduced below for those interested. Sections 1.10.32 and 1.10.33 from "de Finibus Bonorum et Malorum" by Cicero are also reproduced in their exact original form.</p>
    </section>

    <div class="signature" role="img" aria-label="Handwritten signature of the sender"></div>

    <div class="letterhead__footer-rule"></div>
  </main>
</body>
</html>
```